We would like a business card that includes our logo on the front and the following information on the back:

Marcus Keene, Owner
Phone: (555) 614-8027
email: mkeenefencing@postvale.net

Marty Keene & Sons Fencing provides the following services:
Barbed wire
Smooth wire
High tensile
Electric

On the bottom of the card please add:
Please call or email Marcus for estimates.

```html
<!DOCTYPE html>
<html lang="en">
<head>
<meta charset="UTF-8">
<title>Marty Keene &amp; Sons Fencing — Business Card</title>
<link href="https://fonts.googleapis.com/css2?family=Cinzel:wght@600&family=Montserrat:wght@400;500;600&display=swap" rel="stylesheet">
<style>
  :root {
    --bg: #e9e6e2;
    --brown: #7a5439;
    --ink: #2a2420;
    --paper: #ffffff;
    --rule: #8a8580;
  }
  * { box-sizing: border-box; margin: 0; padding: 0; }
  html, body { width: 1200px; height: 786px; overflow: hidden; }
  body {
    background: var(--bg);
    font-family: "Montserrat", sans-serif;
    display: flex;
    align-items: center;
    justify-content: center;
    gap: 40px;
  }
  .card {
    width: 540px;
    height: 309px;
    position: relative;
    box-shadow: 0 6px 18px rgba(0,0,0,.18);
    overflow: hidden;
  }

  /* Front */
  .card--front { background: var(--paper); color: var(--ink); }
  .brand {
    display: flex;
    flex-direction: column;
    align-items: center;
  }
  .brand__name {
    font-family: "Cinzel", serif;
    font-weight: 600;
    font-size: 27px;
    letter-spacing: .5px;
    text-align: center;
    line-height: 1.25;
  }
  .brand__rule {
    width: 290px;
    height: 1px;
    margin-top: 6px;
  }
  .card--front .brand { position: absolute; top: 58px; left: 0; right: 0; }
  .card--front .brand__name { color: var(--ink); }
  .card--front .brand__rule { background: var(--rule); }

  .contact {
    position: absolute;
    top: 178px;
    left: 0; right: 0;
    display: flex;
    justify-content: center;
    align-items: center;
    gap: 18px;
  }
  .person { text-align: right; }
  .person__name {
    font-family: "Cinzel", serif;
    font-weight: 600;
    font-size: 22px;
    color: var(--brown);
    line-height: 1;
  }
  .person__role { font-size: 12px; color: var(--ink); margin-top: 3px; }
  .contact__divider { width: 1px; height: 40px; background: var(--rule); }
  .contact__list { list-style: none; font-size: 13px; color: var(--ink); }
  .contact__list li { display: flex; align-items: center; gap: 8px; line-height: 1.55; }
  .contact__list svg { width: 11px; height: 11px; fill: var(--brown); flex: none; }

  .cta-band {
    position: absolute;
    left: 0; right: 0;
    bottom: 24px;
    height: 34px;
    background: var(--brown);
    color: var(--paper);
    font-size: 13px;
    font-weight: 500;
    display: flex;
    align-items: center;
    justify-content: center;
    letter-spacing: .3px;
  }

  /* Back */
  .card--back { background: var(--brown); color: var(--paper); }
  .card--back .brand { position: absolute; top: 70px; left: 0; right: 0; }
  .card--back .brand__rule { background: rgba(255,255,255,.75); }
  .services {
    position: absolute;
    top: 180px; left: 30px; right: 30px;
    text-align: center;
  }
  .services__title {
    display: flex;
    align-items: center;
    gap: 14px;
    font-size: 13px;
    font-weight: 600;
  }
  .services__title::before, .services__title::after {
    content: "";
    flex: 1;
    height: 1px;
    background: rgba(255,255,255,.75);
  }
  .services__list {
    list-style: none;
    display: flex;
    justify-content: center;
    align-items: center;
    flex-wrap: nowrap;
    margin-top: 16px;
    font-size: 12px;
  }
  .services__list li + li::before {
    content: "";
    display: inline-block;
    width: 6px; height: 6px;
    border-radius: 50%;
    background: var(--paper);
    margin: 0 12px;
    vertical-align: middle;
  }
</style>
</head>
<body>

  <section class="card card--front" aria-label="Business card front">
    <div class="brand">
      <p class="brand__name">Marty Keene &amp; Sons<br>Fencing</p>
      <div class="brand__rule"></div>
    </div>

    <div class="contact">
      <div class="person">
        <p class="person__name">Marcus Keene</p>
        <p class="person__role">Owner</p>
      </div>
      <div class="contact__divider"></div>
      <ul class="contact__list">
        <li>
          <svg viewBox="0 0 24 24" aria-hidden="true"><path d="M6.6 10.8a15 15 0 0 0 6.6 6.6l2.2-2.2c.3-.3.7-.4 1-.2 1.1.4 2.3.6 3.6.6.6 0 1 .4 1 1V20c0 .6-.4 1-1 1A17 17 0 0 1 3 4c0-.6.4-1 1-1h3.5c.6 0 1 .4 1 1 0 1.3.2 2.5.6 3.6.1.3 0 .7-.2 1z"/></svg>
          (555) 614-8027
        </li>
        <li>
          <svg viewBox="0 0 24 24" aria-hidden="true"><path d="M2 5h20v14H2zm2 2v.5l8 5 8-5V7zm0 2.9V17h16V9.9l-8 5z"/></svg>
          mkeenefencing@postvale.net
        </li>
      </ul>
    </div>

    <div class="cta-band">Please call or email Marcus for estimates</div>
  </section>

  <section class="card card--back" aria-label="Business card back">
    <div class="brand">
      <p class="brand__name">Marty Keene &amp; Sons<br>Fencing</p>
      <div class="brand__rule"></div>
    </div>

    <div class="services">
      <p class="services__title">Our Services</p>
      <ul class="services__list">
        <li>Barbed wire</li>
        <li>Barbed wire</li>
        <li>Smooth wire</li>
        <li>High tensile</li>
        <li>Electric</li>
      </ul>
    </div>
  </section>

</body>
</html>
```